Modern Dental Appointment Reminder/Business Card

We already have a beautiful logo and icon picked from here on PixelHarbor, now we need someone to make them into a beautiful business card for us! This business card will also function as an appointment reminder card for patients. It will be double sided and must include:
Front
-Contact Info as Follows:
(Gavin T Morrow, DDS
Family and Cosmetic Dentistry
2947 S 3260 E Ste 400
Cedarvale, Oregon 97451)
-Our Logo or Icon (your choice, if Icon must write "Bluefern Dental" below it like in the example file)
Back
-"You're Invited!"
-"Your next appointment is on"
-Place to write date & time
-"Please call 24hrs ahead if appointment is to be cancelled
-Our Icon

Logo and Icon to be used are attached below, along with an example of what we need.
Please do NOT use lots of red! We want the red to just be an accent. Please use grey, white, or even a muted teal for the majority of the card.

Industry/Entity Type

Dentistry

Contact Information for Business Card

Gavin T Morrow, DDS
2947 S 3260 E Ste 400
Cedarvale, Oregon 97451

Colors
cfeae6

Requirements
Should not have
• Lots of red!

```html
<!DOCTYPE html>
<html lang="en">
<head>
<meta charset="utf-8">
<title>Bluefern Dental – Business &amp; Appointment Card</title>
<link rel="stylesheet" href="https://fonts.googleapis.com/css2?family=Montserrat:wght@400;500;700;800&display=swap">
<style>
  :root {
    --stage: #e9ecec;
    --card: #ffffff;
    --card-edge: #cfeae6;
    --charcoal: #57534e;
    --accent-red: #a8262b;
    --text-grey: #5a5753;
  }
  * { box-sizing: border-box; margin: 0; padding: 0; }
  html, body {
    width: 1200px; height: 913px; overflow: hidden;
    background: var(--stage);
    font-family: "Montserrat", sans-serif;
    color: var(--text-grey);
  }
  .stage { position: relative; width: 1200px; height: 913px; }
  .card {
    position: absolute; left: 250px; width: 700px; height: 400px;
    background: var(--card);
    border-radius: 18px;
    box-shadow: 0 6px 0 var(--card-edge), 0 12px 24px rgba(0,0,0,0.12);
  }
  .card--front { top: 36px; }
  .card--back { top: 470px; }

  /* Front */
  .brand-mark {
    position: absolute; left: 282px; top: 48px;
    width: 136px; height: 136px; border-radius: 50%;
    background: var(--charcoal);
  }
  .brand-name {
    position: absolute; left: 0; right: 0; top: 200px;
    text-align: center; font-weight: 800; font-size: 34px;
    color: var(--charcoal); letter-spacing: 0.5px;
  }
  .doctor { position: absolute; left: 56px; top: 290px; }
  .doctor__name { font-weight: 700; font-size: 27px; color: var(--accent-red); }
  .doctor__title { font-size: 17px; margin-top: 4px; letter-spacing: 0.3px; }
  .address-block {
    position: absolute; left: 392px; top: 288px;
    display: flex; align-items: center; gap: 14px;
  }
  .address-square { width: 24px; height: 54px; background: var(--accent-red); }
  .address { font-size: 18px; line-height: 1.35; font-style: normal; }

  /* Back */
  .invite { position: absolute; left: 40px; top: 60px; color: var(--charcoal); }
  .invite__headline { font-weight: 800; font-size: 33px; line-height: 1; }
  .invite__sub { font-weight: 700; font-size: 14px; margin-top: 8px; }
  .back-brand {
    position: absolute; left: 340px; top: 24px; width: 110px;
    display: flex; flex-direction: column; align-items: center; gap: 6px;
  }
  .back-brand__mark { width: 84px; height: 84px; border-radius: 50%; background: var(--charcoal); }
  .back-brand__name { font-weight: 800; font-size: 12px; color: var(--charcoal); white-space: nowrap; }
  .card--back .address { position: absolute; left: 468px; top: 44px; font-size: 17px; }
  .banner { position: absolute; left: 225px; top: 150px; width: 250px; height: 40px; }
  .banner__label {
    position: absolute; inset: 0;
    display: flex; align-items: center; justify-content: center;
    color: #fff; font-weight: 800; font-size: 19px; letter-spacing: 0.5px;
  }
  .fields { position: absolute; left: 48px; right: 40px; top: 222px; font-size: 19px; }
  .field-row { display: flex; align-items: flex-end; gap: 8px; height: 40px; }
  .field-line { flex: 1; border-bottom: 2px dotted var(--text-grey); height: 1px; margin-bottom: 6px; }
  .field-line--short { flex: 0 0 150px; }
  .notice {
    position: absolute; left: 0; right: 0; bottom: 36px;
    text-align: center; font-size: 17px; letter-spacing: 0.3px;
  }
</style>
</head>
<body>
<main class="stage">

  <section class="card card--front" aria-label="Card front">
    <div class="brand-mark" aria-hidden="true"></div>
    <h1 class="brand-name">Bluefern Dental</h1>
    <div class="doctor">
      <p class="doctor__name">Gavin T Morrow, DDS</p>
      <p class="doctor__title">Family and Cosmetic Dentistry</p>
    </div>
    <div class="address-block">
      <span class="address-square" aria-hidden="true"></span>
      <address class="address">2947 S 3260 E Ste 400<br>Cedarvale, Oregon 97451</address>
    </div>
  </section>

  <section class="card card--back" aria-label="Card back">
    <div class="invite">
      <p class="invite__headline">You're Invited!</p>
      <p class="invite__sub">Your next appointment is on</p>
    </div>
    <div class="back-brand">
      <span class="back-brand__mark" aria-hidden="true"></span>
      <span class="back-brand__name">Bluefern Dental</span>
    </div>
    <address class="address">2947 S 3260 E Ste 400<br>Cedarvale, Oregon 97451</address>

    <div class="banner">
      <svg width="250" height="40" viewBox="0 0 250 40" aria-hidden="true">
        <path d="M8 4 Q125 -2 242 4 Q236 20 244 36 Q125 42 6 36 Q14 20 8 4 Z" fill="var(--charcoal)"/>
      </svg>
      <span class="banner__label">Next Appointment</span>
    </div>

    <div class="fields">
      <div class="field-row"><span>Name:</span><span class="field-line"></span></div>
      <div class="field-row">
        <span>Date:</span><span class="field-line"></span>
        <span>Time:</span><span class="field-line field-line--short"></span><span>(AM/PM)</span>
      </div>
    </div>
    <p class="notice">Please call 24hrs ahead if appointment is to be cancelled</p>
  </section>

</main>
</body>
</html>
```